Garden Maintenance business card

I need a business card design for my new business "Silver Birch Garden Co". I do garden maintenance including lawns, turf lawn, pruning, hedging, water systems, anything related to the garden really (dont think i need to include any of that except garden maintenance)

Reason: narrowed it down and just showing my business partners the designs, cheers

Industry/Entity Type

Business

Requirements
Must have
• Must Have:
- ABN: XX XXX XXX XXX
Mobile phone number 00 0000000
email address xxxx.xxxxxx@gmail.com
Owner Name Xxxx xxxxxx
title: garden specialist possibly under name or something sounding professional
logo which has been submitted both with a background and one without, feel free to choose whichever one you like
business name

```html
<!DOCTYPE html>
<html lang="en">
<head>
<meta charset="utf-8">
<title>Silver Birch Garden Co — Business Card</title>
<link rel="stylesheet" href="https://fonts.googleapis.com/css2?family=Exo+2:wght@400;600;700&display=swap">
<style>
  :root {
    --stage: #2b2b2b;
    --card: #f4f4f2;
    --card-edge: #e6e7e3;
    --ink: #1f2a22;
    --leaf: #1e8a4c;
    --wash-sage: #c9d6b4;
    --wash-grey: #b9c4c0;
    --muted: #9a9d9a;
    --rule: #c9ccc8;
  }
  * { box-sizing: border-box; margin: 0; padding: 0; }
  html, body {
    width: 1200px; height: 890px; overflow: hidden;
    background: var(--stage);
    font-family: "Exo 2", sans-serif;
  }
  .stage {
    position: relative; width: 1200px; height: 890px;
    display: flex; justify-content: center; align-items: center; gap: 80px;
  }
  .card {
    position: relative; width: 370px; height: 620px;
    background: var(--card); border-radius: 22px; overflow: hidden;
  }

  /* back: contact side */
  .card-back .wash-top {
    position: absolute; left: 0; top: 0; width: 100%; height: 150px;
    background: linear-gradient(180deg, var(--wash-sage) 0%, var(--wash-grey) 45%, rgba(244,244,242,0) 100%);
    opacity: .7;
  }
  .card-back .brand {
    position: absolute; right: 26px; top: 34px;
    font-size: 28px; font-weight: 600; color: var(--ink); text-align: right;
  }
  .card-back .person { position: absolute; left: 36px; top: 300px; }
  .person .name { font-size: 30px; font-weight: 700; color: var(--ink); letter-spacing: .5px; }
  .person .role { font-size: 19px; font-weight: 600; color: var(--leaf); margin-top: 2px; }
  .contact { position: absolute; left: 36px; top: 420px; font-size: 17px; color: var(--ink); line-height: 1.25; }
  .contact .label { color: var(--leaf); font-weight: 700; }
  .rule { position: absolute; left: 36px; right: 26px; top: 475px; height: 1px; background: var(--rule); }
  .abn { position: absolute; left: 36px; top: 498px; font-size: 14px; color: var(--muted); letter-spacing: .5px; }

  /* front: brand side */
  .card-front .wash {
    position: absolute; left: 20px; top: 30px; width: 330px; height: 520px;
    background: radial-gradient(ellipse at 55% 45%, var(--wash-sage) 0%, var(--wash-grey) 45%, rgba(244,244,242,0) 75%);
    opacity: .75;
  }
  .card-front .illustration {
    position: absolute; left: 140px; top: 90px; width: 200px; height: 300px;
    border-radius: 12px;
    background: linear-gradient(180deg, #4f8a4a 0%, #8fb07a 30%, #e7ddd0 55%, #d9cbb8 100%);
  }
  .card-front .brand {
    position: absolute; right: 30px; top: 470px; width: 300px;
    font-size: 38px; font-weight: 700; color: var(--ink); text-align: right; line-height: 1.05;
  }
</style>
</head>
<body>
<main class="stage">
  <section class="card card-back" aria-label="Business card, contact side">
    <div class="wash-top"></div>
    <div class="brand">Silver Birch Garden Co</div>
    <div class="person">
      <div class="name">DEAN HOLLOWAY</div>
      <div class="role">Garden Specialist</div>
    </div>
    <div class="contact">
      <div><span class="label">Mobile:</span> +75 5550 218</div>
      <div><span class="label">Email:</span> dean.hollo@mail.com</div>
    </div>
    <div class="rule"></div>
    <div class="abn">ABN: 98 204 315 760</div>
  </section>

  <section class="card card-front" aria-label="Business card, brand side">
    <div class="wash"></div>
    <div class="illustration" role="img" aria-label="Illustration of a thumbs-up hand with a small leafy tree growing from the green thumb"></div>
    <div class="brand">Silver Birch Garden Co</div>
  </section>
</main>
</body>
</html>
```